Pharmacy handmade, Personalized Medical Cosmetics Label

Medical Cosmetics label, elegant and professional looking. The creams are Dermatologist formulated and are prepared by local Pharmacy. The label should be versatile and allow space for hand writing to be filled by the pharmacist preparing the product.
The following information will be handwritten:
Upper lid - Eye Care No.3 ; Marigold, Retinol ; 30
Lower Bottom - Teodora Brandt ; Signature ; 01.01.2017
Upper Lid Label
Vella Skin (logo)
Doctor Series
(circular pattern - Doctor Formulated, Registered Pharmacy, Handmade, Highest Medical Standards)
(Eye Care No.3 - in hand writing and different color, maybe red)
Key Ingredients: (Marigold, Retinol - in hand writing, same color as above, maybe red)
(box with hand writing 30) ml
Lower Bottom Label (underneath surface of the container)
Made for Vella Skin by
Pharmacy Estrel, 7 Kalina blvd., Sofia, ph. 0893517640
Patient: (Teodora Brandt- in hand writing)
Pharmacist: (Signature - in hand writing)
Date: (01.01.2017 - in hand writing)
For External Use
good for 60 days after preparation
Ingredients: Retinol, Marigold Extract, Water, Glycerin, Stearyl Alcohol, Wheat Germ Oil, Polysorbate 60, Sesame Oil, Myristyl Myristate, Cetyl Alcohol, Sorbitan Stearate, Phenoxyethanol, Calendula Extract, Cornflower Extract, Sodium Alginate, Sodium Citrate.
The container lid and bottom are 5 cm = 50 mm in diameter. Made from aluminum and contain 30ml or 50ml.
Please refer to the screen shots from my Web Site to get the feeling for the color pallet and professional look. These creams will be sold on this website. They are custom made by a registered Pharmacy right on the spot after the order has been placed. This is why I need more space for the hand written notes made by the pharmacist who prepared the order.
Please make the design professional, simple and serious colors, like light brown, beige, black or dark brown letters, red hand writing (will be filled by pen or thin marker by the Pharmacist by hand, depending on the order, patient name, etc.)
Thank you.
Target Market(s)
female 24 - 49 year old
Industry/Entity Type
Medical

```html
<!DOCTYPE html>
<html lang="en">
<head>
<meta charset="utf-8">
<title>Vella Skin – Doctor Series Labels</title>
<link rel="stylesheet" href="https://fonts.googleapis.com/css2?family=Poppins:wght@600;700&family=Questrial&display=swap">
<style>
  :root {
    --red: #ec2227;
    --brown-dark: #2c221d;
    --brown: #4a372e;
    --ring-brown: #6e4c37;
    --rule: #8c6d58;
    --cream: #f4eee7;
    --ring-text: #3a2a22;
    --page: #ffffff;
  }
  * { margin: 0; padding: 0; box-sizing: border-box; }
  html, body { width: 1200px; height: 400px; overflow: hidden; background: var(--page); }
  .canvas { position: relative; width: 1200px; height: 400px; font-family: "Questrial", sans-serif; }

  /* Lid label */
  .lid-label { position: absolute; left: 0; top: 0; width: 400px; height: 400px; }
  .ring-text { font-family: "Questrial", sans-serif; font-size: 19px; fill: var(--ring-text); }
  .lid-brand { font-family: "Questrial", sans-serif; font-size: 24px; fill: var(--cream); }
  .lid-series { font-family: "Questrial", sans-serif; font-size: 13px; fill: var(--cream); }
  .lid-field-label { font-family: "Questrial", sans-serif; font-size: 13.5px; fill: var(--cream); }

  /* Bottom label */
  .bottom-label { position: absolute; left: 400px; top: 66px; width: 734px; height: 204px; }
  .bottom-label .rule { position: absolute; left: 0; width: 100%; height: 2px; background: var(--rule); }
  .rule.top { top: 0; }
  .rule.under-1 { top: 196px; }
  .rule.under-2 { top: 202px; }
  .label-band { position: absolute; left: 0; top: 6px; width: 100%; height: 188px; background: var(--brown-dark); }
  .label-header { position: absolute; left: 0; top: 0; width: 100%; height: 42px; background: var(--brown); border-bottom: 1px solid var(--rule); }
  .made-for { position: absolute; left: 18px; top: 24px; font-family: "Poppins", sans-serif; font-weight: 600; font-size: 11px; color: var(--cream); }
  .band-brand { position: absolute; right: 64px; top: 12px; font-size: 16px; color: var(--cream); }
  .pharmacy-line { position: absolute; left: 18px; top: 45px; font-size: 12px; color: var(--cream); }
  .pharmacy-line strong { font-family: "Poppins", sans-serif; font-weight: 700; }
  .band-series { position: absolute; right: 16px; top: 44px; font-size: 13px; color: var(--cream); }
  .write-in { position: absolute; left: 18px; width: 700px; height: 20px; background: var(--red); color: var(--cream); font-size: 13px; line-height: 20px; padding-left: 14px; }
  .write-in.patient { top: 66px; }
  .write-in.pharmacist { top: 90px; }
  .write-in.date { top: 114px; }
  .ingredients { position: absolute; left: 18px; top: 140px; width: 700px; font-size: 9.6px; line-height: 14px; color: var(--cream); }
  .ingredients span { display: block; text-align: justify; text-align-last: justify; white-space: nowrap; }
  .ingredients span.last { text-align-last: left; }
  .ingredients strong { font-family: "Poppins", sans-serif; font-weight: 700; }
  .usage-note { position: absolute; right: 16px; top: 168px; font-family: "Poppins", sans-serif; font-weight: 700; font-size: 11px; color: var(--cream); }
</style>
</head>
<body>
<div class="canvas">

  <svg class="lid-label" viewBox="0 0 400 400" aria-label="Lid label">
    <defs>
      <clipPath id="upper-half"><rect x="0" y="0" width="400" height="142"/></clipPath>
      <path id="arc-top" d="M 42 200 A 146 146 0 0 1 334 200"/>
      <path id="arc-bottom" d="M 28 200 A 160 160 0 0 0 348 200"/>
    </defs>

    <circle cx="188" cy="200" r="170" fill="var(--page)" stroke="var(--ring-brown)" stroke-width="5"/>
    <circle cx="188" cy="200" r="131" fill="var(--brown-dark)"/>
    <circle cx="188" cy="200" r="131" fill="var(--brown)" clip-path="url(#upper-half)"/>
    <line x1="80" y1="142" x2="318" y2="142" stroke="var(--cream)" stroke-width="1.2"/>

    <text class="ring-text"><textPath href="#arc-top" startOffset="110" text-anchor="middle" textLength="196">Doctor Formulated</textPath></text>
    <text class="ring-text"><textPath href="#arc-top" startOffset="347" text-anchor="middle" textLength="199">Registered Pharmacy</textPath></text>
    <text class="ring-text"><textPath href="#arc-bottom" startOffset="90" text-anchor="middle" textLength="120">Handmade</textPath></text>
    <text class="ring-text"><textPath href="#arc-bottom" startOffset="343" text-anchor="middle" textLength="285">Highest Medical Standards</textPath></text>

    <g fill="var(--ring-text)">
      <circle cx="188" cy="52" r="6"/>
      <circle cx="40" cy="200" r="6"/>
      <circle cx="336" cy="200" r="6"/>
      <circle cx="122" cy="330" r="6"/>
    </g>

    <text class="lid-brand" x="188" y="120" text-anchor="middle">Vella Skin</text>
    <text class="lid-series" x="316" y="158" text-anchor="end">Doctor Series</text>

    <rect class="write-in-product" x="76" y="188" width="248" height="20" fill="var(--red)"/>
    <text class="lid-field-label" x="88" y="233">Key Ingredients:</text>
    <rect class="write-in-ingredients" x="196" y="219" width="128" height="21" fill="var(--red)"/>
    <rect class="write-in-ingredients" x="86" y="246" width="230" height="19" fill="var(--red)"/>
    <circle class="write-in-volume" cx="192" cy="306" r="16" fill="var(--red)"/>
    <text class="lid-field-label" x="210" y="314">ml</text>
  </svg>

  <section class="bottom-label" aria-label="Bottom label">
    <div class="rule top"></div>
    <div class="label-band">
      <div class="label-header">
        <p class="made-for">Made for Vella Skin by</p>
        <p class="band-brand">Vella Skin</p>
      </div>
      <p class="pharmacy-line"><strong>Pharmacy Estrel</strong>, 7 Kalina blvd., Sofia, ph. 0893517640</p>
      <p class="band-series">Doctor Series</p>
      <div class="write-in patient">Patient:</div>
      <div class="write-in pharmacist">Pharmacist:</div>
      <div class="write-in date">Date:</div>
      <p class="ingredients">
        <span><strong>Ingredients:</strong> Retinol, Marigold Extract, Water, Glycerin, Stearyl Alcohol, Wheat Germ Oil, Polysorbate 60, Sesame Oil, Myristyl</span>
        <span>Myristate, Cetyl Alcohol, Sorbitan Stearate, Phenoxyethanol, Calendula Extract, Cornflower Extract, Sodium Alginate, Sodium</span>
        <span class="last">Citrate.</span>
      </p>
      <p class="usage-note">For External Use&nbsp; good for 60 days after preparation</p>
    </div>
    <div class="rule under-1"></div>
    <div class="rule under-2"></div>
  </section>

</div>
</body>
</html>
```